CREST Academy Exhibit Booth Posters

My company is CREST Academy (a division of CREST for Growth). We are exhibiting in a month, and I need to re-do my exhibit booth posters. There will be a total of 4 posters needed. Sizes are below.
1) Top- 11 feet long X 12 inches wide (Try to match color scheme in example photo)
2) Center- 4 feet long X 2 feet wide (Chalkboard background)
3) Left- 18 inches long X 2 feet wide (Cork-board back ground with the use of push pins holding up post-it-notes, paper, etc.)
4) Right- 18 inches long X 2 feet wide (Cork-board back ground with the use of push pins holding up post-it-notes, paper, etc.)
I have attached a photo of my old booth. This will get you an idea of the size, color schemes, and more. I have created basic rendering of each poster. The content is important, but the look and design should be drastically improved.
The websites to look into for ideas are:
www.crestforgrowth.example
www.crestacademy.example
Updates
I've added a new file. It's a .JPG of the certification diploma. Thanks!
Target Market(s)
Business Owners, Managers, HR, Supervisors, Teens who want to boost their resume
Industry/Entity Type
It Company
Look and feel

```html
<!DOCTYPE html>
<html lang="en">
<head>
<meta charset="utf-8">
<title>CREST Academy – Booth Header Banner</title>
<link href="https://fonts.googleapis.com/css2?family=Tinos:wght@700&display=swap" rel="stylesheet">
<style>
  :root {
    --blush: #f7dfe3;
    --rose: #ec8f9c;
    --crimson: #d2283e;
    --berry: #8e1f45;
    --navy: #1c1f5c;
    --deep-navy: #0d1240;
    --sky: #9fd3ef;
    --white: #ffffff;
    --brand-blue: #2a58b8;
    --brand-red: #c4213a;
  }
  html, body {
    margin: 0;
    padding: 0;
    overflow: hidden;
    background: var(--white);
  }
  .banner {
    position: relative;
    width: 1200px;
    height: 100px;
    overflow: hidden;
    background: linear-gradient(90deg,
      var(--blush) 0%,
      var(--rose) 22%,
      var(--crimson) 42%,
      var(--berry) 62%,
      var(--navy) 80%,
      var(--deep-navy) 100%);
    font-family: "Tinos", "Times New Roman", serif;
  }
  .banner__waves {
    position: absolute;
    inset: 0;
    width: 1200px;
    height: 100px;
  }
  .brand-badge {
    position: absolute;
    left: 8px;
    top: 22px;
    display: flex;
    align-items: center;
    gap: 6px;
  }
  .brand-badge__dot {
    width: 20px;
    height: 20px;
    border-radius: 50%;
    background: var(--brand-blue);
  }
  .brand-badge__name {
    font-size: 17px;
    font-weight: 700;
    line-height: 1.05;
    color: var(--brand-red);
    width: 80px;
  }
  .brand-wordmark {
    position: absolute;
    left: 185px;
    top: 10px;
    font-size: 52px;
    font-weight: 700;
    color: var(--brand-blue);
    letter-spacing: 1px;
    white-space: nowrap;
  }
  .tagline {
    position: absolute;
    left: 664px;
    top: 5px;
    margin: 0;
    font-size: 29px;
    font-weight: 700;
    line-height: 40px;
    color: var(--white);
    text-shadow: 2px 2px 2px rgba(0, 0, 0, 0.55);
    white-space: nowrap;
  }
  .tagline span { display: block; }
</style>
</head>
<body>
  <header class="banner">
    <svg class="banner__waves" viewBox="0 0 1200 100" aria-hidden="true">
      <path d="M0 66 C250 84 550 94 850 93 C1000 92 1120 88 1200 85 L1200 100 L0 100 Z" fill="#ffffff" opacity="0.85"/>
      <path d="M0 80 C260 94 560 98 860 97 C1010 96 1120 93 1200 91 L1200 100 L0 100 Z" fill="var(--sky)" opacity="0.85"/>
      <path d="M0 60 C250 78 550 90 850 90 C1000 89 1120 85 1200 82" fill="none" stroke="#ffffff" stroke-width="2" opacity="0.8"/>
      <path d="M0 94 C300 100 640 99 960 99 C1080 99 1150 98 1200 97 L1200 100 L0 100 Z" fill="#ffffff"/>
    </svg>

    <div class="brand-badge">
      <span class="brand-badge__dot"></span>
      <span class="brand-badge__name">CREST Academy</span>
    </div>

    <div class="brand-wordmark">CREST Academy</div>

    <h1 class="tagline">
      <span>Training School for a Workforce</span>
      <span>with&nbsp; Limited Work Experience</span>
    </h1>
  </header>
</body>
</html>
```